Animal Puzzle game Needs Design

Need a redesign of the UI of this puzzle game and a forest background. This game is for any age. The design needs to be on separate layers in Photoshop. The design needs to be colorful and easy to see the different UI parts, sound control, progress bar, number of lives and number of moves.

Target Market(s)

All ages

Requirements
Must have
• Needs to have each of the UI elements and a background.

```html
<!DOCTYPE html>
<html lang="en">
<head>
<meta charset="utf-8">
<title>Animal Puzzle – Game UI</title>
<link href="https://fonts.googleapis.com/css2?family=Luckiest+Guy&family=Arimo:wght@400;700&display=swap" rel="stylesheet">
<style>
  :root{
    --board:#f2f2f2;
    --white:#ffffff;
    --label-shadow:#2c3b1a;
    --lives-red:#e8173a;
    --level-green:#2fc23a;
    --moves-yellow:#f2cf12;
    --cell:#f0f0f0;
    --cell-line:#e2e2e2;
    --purple:#8a1fd6;
    --purple-dark:#6a10b0;
    --bar-grey:#d9d9d9;
    --sound-blue:#1b9ad6;
    --guide:#33e6f0;
    --panel:#535353;
    --panel-dark:#3c3c3c;
    --panel-line:#2e2e2e;
    --panel-text:#e6e6e6;
    --panel-select:#5b6e86;
    --display:"Luckiest Guy","Arial Black",Impact,sans-serif;
  }
  *{box-sizing:border-box;margin:0;padding:0}
  html,body{width:1200px;height:1000px;overflow:hidden;background:var(--board)}
  .board{position:relative;width:1200px;height:1000px}

  /* game screens */
  .screen{position:absolute;width:610px;height:528px;overflow:hidden;box-shadow:3px 4px 7px rgba(0,0,0,.45)}
  .screen--play{left:522px;top:402px;width:608px;z-index:1}
  .screen--main{left:70px;top:70px;z-index:2}
  .screen--grid{left:70px;top:641px;transform:scale(.5443);transform-origin:0 0;z-index:1}
  .forest{position:absolute;inset:0;
    background:linear-gradient(180deg,#7d8a3a 0%,#6c7f2f 18%,#5d8a3e 38%,#4c9a6a 55%,#5f7fb0 64%,#3b8a34 74%,#2f7a23 88%,#24621a 100%)}
  .hud-label{position:absolute;width:120px;text-align:center;font-family:var(--display);font-weight:700;
    text-transform:uppercase;font-size:16px;line-height:18px;color:var(--white);letter-spacing:.5px;
    text-shadow:1px 2px 0 var(--label-shadow)}
  .hud-icon{position:absolute}
  .hud-icon text{font-family:var(--display);font-weight:700;font-size:14px;fill:var(--white)}

  .puzzle{position:absolute;left:105px;top:125px;width:398px;height:294px;border:4px solid var(--white);
    border-radius:8px;overflow:hidden;background:var(--cell)}
  .puzzle__grid{position:absolute;inset:0;display:grid;grid-template-columns:repeat(7,1fr);
    grid-template-rows:repeat(6,1fr);gap:1px;background:var(--cell-line)}
  .puzzle__grid span{background:var(--cell)}
  .puzzle__photo{position:absolute;inset:0;
    background:radial-gradient(ellipse 45% 55% at 50% 60%,#6a4a2e 0%,#8a6440 45%,#a98a66 70%,#d8d4cc 100%)}
  .puzzle__lines{position:absolute;inset:0;
    background:
      repeating-linear-gradient(90deg,transparent 0 55.4px,rgba(255,255,255,.7) 55.4px 56.4px),
      repeating-linear-gradient(180deg,transparent 0 47.6px,rgba(255,255,255,.7) 47.6px 48.6px)}

  .progress-label{position:absolute;left:234px;top:438px;width:140px;text-align:center;
    font-family:var(--display);font-weight:700;text-transform:uppercase;font-size:16px;line-height:18px;
    color:var(--white);text-shadow:1px 2px 0 var(--label-shadow)}
  .progress{position:absolute;left:105px;top:461px;width:397px;height:37px;border:3px solid var(--white);
    border-radius:10px;overflow:hidden;background:linear-gradient(180deg,#f4f4f4 0%,var(--bar-grey) 60%,#c4c4c4 100%)}
  .progress__fill{position:absolute;left:0;top:0;bottom:0;width:72px;border-radius:7px 0 0 7px;
    background:linear-gradient(180deg,#a54ae8 0%,var(--purple) 55%,var(--purple-dark) 100%)}
  .progress__value{position:absolute;inset:0;display:flex;align-items:center;justify-content:center;
    font-family:var(--display);font-weight:700;font-size:14px;color:var(--purple);padding-top:1px}
  .sound{position:absolute;left:515px;top:456px}

  .guides{position:absolute;inset:0;pointer-events:none}
  .guides i{position:absolute;background:var(--guide)}
  .guides .v{top:0;bottom:0;width:2px}
  .guides .h{left:0;right:0;height:2px}

  /* layers panel */
  .layers{position:absolute;left:906px;top:70px;width:224px;height:281px;background:var(--panel);z-index:3;
    box-shadow:3px 4px 7px rgba(0,0,0,.45);font-family:Arimo,Arial,sans-serif;font-size:9.5px;color:var(--panel-text)}
  .layers__tabs{height:18px;background:var(--panel-dark);display:flex;align-items:flex-end}
  .layers__tab{padding:3px 7px;color:#aaa}
  .layers__tab--active{background:var(--panel);color:var(--panel-text)}
  .layers__row{display:flex;align-items:center;gap:6px;padding:0 6px;height:28px;border-bottom:1px solid var(--panel-line)}
  .field{background:#6a6a6a;border:1px solid #2c2c2c;height:18px;padding:0 5px;display:flex;align-items:center;justify-content:space-between}
  .field--light{background:#ececec;color:#222;border-color:#888}
  .layer{display:flex;align-items:center;height:23px;border-top:1px solid var(--panel-line)}
  .layer__eye{width:30px;display:flex;justify-content:center;border-right:1px solid var(--panel-line);height:100%;align-items:center}
  .layer__name{margin-left:6px}
  .layer--selected{height:36px;background:var(--panel-select)}
  .thumb{width:34px;height:30px;margin-left:6px;border:1px solid #222;background:linear-gradient(180deg,#8a8a3a,#3a8a4a 60%,#2a6a1e)}
</style>
</head>
<body>
<main class="board">

  <!-- play screen with animal photo (behind) -->
  <section class="screen screen--play">
    <div class="forest" role="img" aria-label="Painted forest background with tall trees, bluebells and grass"></div>
    <div class="hud-label" style="left:243px;top:24px">Level</div>
    <svg class="hud-icon" style="left:279px;top:44px" width="48" height="48" viewBox="0 0 48 48">
      <circle cx="24" cy="24" r="21.5" fill="var(--level-green)" stroke="#fff" stroke-width="3"/>
      <text x="24" y="31" text-anchor="middle" font-size="18">2</text>
    </svg>
    <div class="hud-label" style="left:486px;top:24px">Moves</div>
    <svg class="hud-icon" style="left:520px;top:43px" width="54" height="52" viewBox="0 0 54 52">
      <polygon points="27,3 33.5,18.5 50,19.5 37.5,30.5 41.5,47 27,38 12.5,47 16.5,30.5 4,19.5 20.5,18.5" fill="var(--moves-yellow)" stroke="#fff" stroke-width="3" stroke-linejoin="round"/>
      <text x="27" y="33" text-anchor="middle" font-size="11">10</text>
    </svg>
    <div class="puzzle" style="height:295px">
      <div class="puzzle__photo" role="img" aria-label="Photograph of a brown bear split into puzzle tiles"></div>
      <div class="puzzle__lines"></div>
    </div>
    <div class="progress-label" style="top:440px">Progress</div>
    <div class="progress" style="top:462px"><div class="progress__fill" style="width:71px"></div><div class="progress__value">28/100</div></div>
    <svg class="sound" style="left:512px;top:456px" width="58" height="48" viewBox="0 0 58 48">
      <path d="M4 16 H14 L28 4 V44 L14 32 H4Z" fill="var(--sound-blue)" stroke="#fff" stroke-width="3" stroke-linejoin="round"/>
      <path d="M35 16 Q41 24 35 32" fill="none" stroke="#fff" stroke-width="8" stroke-linecap="round"/>
      <path d="M35 16 Q41 24 35 32" fill="none" stroke="var(--sound-blue)" stroke-width="4" stroke-linecap="round"/>
      <path d="M43 8 Q55 24 43 40" fill="none" stroke="#fff" stroke-width="8" stroke-linecap="round"/>
      <path d="M43 8 Q55 24 43 40" fill="none" stroke="var(--sound-blue)" stroke-width="4" stroke-linecap="round"/>
    </svg>
  </section>

  <!-- empty puzzle screen (front) -->
  <section class="screen screen--main">
    <div class="forest" role="img" aria-label="Painted forest background with tall trees, bluebells and grass"></div>
    <div class="hud-label" style="left:3px;top:24px">Lives</div>
    <svg class="hud-icon" style="left:37px;top:45px" width="54" height="48" viewBox="0 0 54 48">
      <path d="M27 45 C10 32 2 24 2 14 C2 6 8 2 15 2 C21 2 25 6 27 9 C29 6 33 2 39 2 C46 2 52 6 52 14 C52 24 44 32 27 45Z" fill="var(--lives-red)" stroke="#fff" stroke-width="3"/>
      <text x="27" y="28" text-anchor="middle">3</text>
    </svg>
    <div class="hud-label" style="left:244px;top:24px">Level</div>
    <svg class="hud-icon" style="left:280px;top:44px" width="48" height="48" viewBox="0 0 48 48">
      <circle cx="24" cy="24" r="21.5" fill="var(--level-green)" stroke="#fff" stroke-width="3"/>
      <text x="24" y="31" text-anchor="middle" font-size="18">2</text>
    </svg>
    <div class="hud-label" style="left:487px;top:24px">Moves</div>
    <svg class="hud-icon" style="left:521px;top:43px" width="54" height="52" viewBox="0 0 54 52">
      <polygon points="27,3 33.5,18.5 50,19.5 37.5,30.5 41.5,47 27,38 12.5,47 16.5,30.5 4,19.5 20.5,18.5" fill="var(--moves-yellow)" stroke="#fff" stroke-width="3" stroke-linejoin="round"/>
      <text x="27" y="33" text-anchor="middle" font-size="11">10</text>
    </svg>
    <div class="puzzle"><div class="puzzle__grid">
      <span></span><span></span><span></span><span></span><span></span><span></span><span></span>
      <span></span><span></span><span></span><span></span><span></span><span></span><span></span>
      <span></span><span></span><span></span><span></span><span></span><span></span><span></span>
      <span></span><span></span><span></span><span></span><span></span><span></span><span></span>
      <span></span><span></span><span></span><span></span><span></span><span></span><span></span>
      <span></span><span></span><span></span><span></span><span></span><span></span><span></span>
    </div></div>
    <div class="progress-label">Progress</div>
    <div class="progress"><div class="progress__fill"></div><div class="progress__value">28/100</div></div>
    <svg class="sound" width="58" height="48" viewBox="0 0 58 48">
      <path d="M4 16 H14 L28 4 V44 L14 32 H4Z" fill="var(--sound-blue)" stroke="#fff" stroke-width="3" stroke-linejoin="round"/>
      <path d="M35 16 Q41 24 35 32" fill="none" stroke="#fff" stroke-width="8" stroke-linecap="round"/>
      <path d="M35 16 Q41 24 35 32" fill="none" stroke="var(--sound-blue)" stroke-width="4" stroke-linecap="round"/>
      <path d="M43 8 Q55 24 43 40" fill="none" stroke="#fff" stroke-width="8" stroke-linecap="round"/>
      <path d="M43 8 Q55 24 43 40" fill="none" stroke="var(--sound-blue)" stroke-width="4" stroke-linecap="round"/>
    </svg>
  </section>

  <!-- screen with guides -->
  <section class="screen screen--grid">
    <div class="forest" role="img" aria-label="Painted forest background with tall trees, bluebells and grass"></div>
    <div class="hud-label" style="left:3px;top:24px">Lives</div>
    <svg class="hud-icon" style="left:37px;top:45px" width="54" height="48" viewBox="0 0 54 48">
      <path d="M27 45 C10 32 2 24 2 14 C2 6 8 2 15 2 C21 2 25 6 27 9 C29 6 33 2 39 2 C46 2 52 6 52 14 C52 24 44 32 27 45Z" fill="var(--lives-red)" stroke="#fff" stroke-width="3"/>
      <text x="27" y="28" text-anchor="middle">3</text>
    </svg>
    <div class="hud-label" style="left:244px;top:24px">Level</div>
    <svg class="hud-icon" style="left:280px;top:44px" width="48" height="48" viewBox="0 0 48 48">
      <circle cx="24" cy="24" r="21.5" fill="var(--level-green)" stroke="#fff" stroke-width="3"/>
      <text x="24" y="31" text-anchor="middle" font-size="18">2</text>
    </svg>
    <div class="hud-label" style="left:487px;top:24px">Moves</div>
    <svg class="hud-icon" style="left:521px;top:43px" width="54" height="52" viewBox="0 0 54 52">
      <polygon points="27,3 33.5,18.5 50,19.5 37.5,30.5 41.5,47 27,38 12.5,47 16.5,30.5 4,19.5 20.5,18.5" fill="var(--moves-yellow)" stroke="#fff" stroke-width="3" stroke-linejoin="round"/>
      <text x="27" y="33" text-anchor="middle" font-size="11">10</text>
    </svg>
    <div class="puzzle" style="border-width:0;border-radius:0;background:var(--cell)"></div>
    <div class="progress-label">Progress</div>
    <div class="progress"><div class="progress__fill"></div><div class="progress__value">28/100</div></div>
    <svg class="sound" width="58" height="48" viewBox="0 0 58 48">
      <path d="M4 16 H14 L28 4 V44 L14 32 H4Z" fill="var(--sound-blue)" stroke="#fff" stroke-width="3" stroke-linejoin="round"/>
      <path d="M35 16 Q41 24 35 32" fill="none" stroke="var(--sound-blue)" stroke-width="4" stroke-linecap="round"/>
      <path d="M43 8 Q55 24 43 40" fill="none" stroke="var(--sound-blue)" stroke-width="4" stroke-linecap="round"/>
    </svg>
    <div class="guides">
      <i class="v" style="left:16px"></i><i class="v" style="left:105px"></i><i class="v" style="left:220px"></i>
      <i class="v" style="left:330px"></i><i class="v" style="left:390px"></i><i class="v" style="left:445px"></i>
      <i class="v" style="left:503px"></i><i class="v" style="left:594px"></i>
      <i class="h" style="top:26px"></i><i class="h" style="top:80px"></i><i class="h" style="top:125px"></i>
      <i class="h" style="top:172px"></i><i class="h" style="top:220px"></i><i class="h" style="top:270px"></i>
      <i class="h" style="top:318px"></i><i class="h" style="top:366px"></i><i class="h" style="top:419px"></i>
      <i class="h" style="top:461px"></i><i class="h" style="top:498px"></i>
    </div>
  </section>

  <!-- layers panel -->
  <aside class="layers">
    <div class="layers__tabs">
      <span class="layers__tab layers__tab--active">Layers</span>
      <span class="layers__tab">Channels</span>
      <span class="layers__tab">Paths</span>
    </div>
    <div class="layers__row"><span class="field" style="width:64px">Kind ⬍</span>
      <svg width="110" height="12" viewBox="0 0 110 12" fill="none" stroke="#ddd"><rect x="2" y="1" width="11" height="10"/><circle cx="32" cy="6" r="5"/><path d="M50 1h10M55 1v10"/><rect x="72" y="2" width="9" height="8"/><rect x="92" y="1" width="9" height="10"/></svg></div>
    <div class="layers__row"><span class="field" style="width:110px">Normal ⬍</span><span>Opacity:</span><span class="field field--light" style="width:52px">100% ▾</span></div>
    <div class="layers__row"><span>Lock:</span>
      <svg width="76" height="12" viewBox="0 0 76 12" fill="#bbb"><rect x="2" y="1" width="10" height="10" opacity=".6"/><path d="M22 11 L31 2 L33 4 L24 12Z"/><path d="M48 0v12M42 6h12" stroke="#bbb" stroke-width="2"/><rect x="64" y="5" width="9" height="7"/></svg>
      <span style="margin-left:auto">Fill:</span><span class="field field--light" style="width:52px">100% ▾</span></div>
    <div class="layer-list">
      <div class="layer"><span class="layer__eye">👁</span><span class="layer__name">▸ ▬ LIVES</span></div>
      <div class="layer"><span class="layer__eye">👁</span><span class="layer__name">▸ ▬ LEVEL</span></div>
      <div class="layer"><span class="layer__eye">👁</span><span class="layer__name">▸ ▬ MOVES</span></div>
      <div class="layer"><span class="layer__eye">👁</span><span class="layer__name">▸ ▬ PUZZLE</span></div>
      <div class="layer"><span class="layer__eye">👁</span><span class="layer__name">▸ ▬ PROGRESS</span></div>
      <div class="layer"><span class="layer__eye">👁</span><span class="layer__name">▸ ▬ SOUND</span></div>
      <div class="layer layer--selected"><span class="layer__eye">👁</span><span class="thumb"></span><span class="layer__name">background</span></div>
    </div>
  </aside>

</main>
</body>
</html>
```